Brochure for medical doctor

I need a brochure for a medical doctor to promote his practice. The brochure should contain his picture, business information (use letterhead from attachment), and the following text:

- Now accepting PI cases on lien!
- Same and next business day appointments available for initial visits, pre-operative clearances, and all other medical needs

- Expedited medical reports sent quickly to your office

Medical

```html
<!DOCTYPE html>
<html lang="en">
<head>
<meta charset="utf-8">
<title>Meadowbrook Medical Center – Flyer</title>
<link rel="stylesheet" href="https://fonts.googleapis.com/css2?family=Tinos:ital,wght@0,400;0,700;1,700&display=swap">
<style>
  :root {
    --page-bg: #ece8e2;
    --paper: #f6f7f1;
    --blue-deep: #1b2d86;
    --blue: #2c55aa;
    --green: #2a9045;
    --green-text: #23803c;
    --white: #ffffff;
  }
  * { box-sizing: border-box; margin: 0; padding: 0; }
  html, body { width: 1200px; height: 900px; overflow: hidden; background: var(--page-bg); }
  body { font-family: "Tinos", "Times New Roman", serif; position: relative; }

  .flyer {
    position: absolute; left: 270px; top: 20px;
    width: 660px; height: 860px;
    background: var(--paper);
    overflow: hidden;
    box-shadow: 0 6px 22px rgba(0,0,0,0.18);
  }
  .flyer-bands { position: absolute; inset: 0; }

  .brand { position: absolute; left: 116px; top: 60px; right: 18px; color: var(--white); }
  .brand-mark {
    position: absolute; left: 38px; top: 120px;
    width: 62px; height: 62px; background: var(--white);
  }
  .brand-name { font-size: 27px; font-weight: 700; letter-spacing: 0.3px; text-transform: uppercase; white-space: nowrap; }
  .brand-contact { font-size: 15px; margin-top: 6px; white-space: nowrap; }

  .services-title {
    position: absolute; left: 300px; top: 222px;
    color: var(--blue); font-size: 30px; font-weight: 700; letter-spacing: 1px;
  }
  .service-list {
    position: absolute; list-style: disc;
    color: var(--green-text); font-style: italic; font-weight: 700; font-size: 21px; line-height: 1.3;
  }
  .service-list--right { left: 410px; top: 268px; width: 240px; }
  .service-list--left { left: 58px; top: 330px; width: 310px; }

  .news-title {
    position: absolute; left: 340px; top: 450px;
    color: var(--white); font-size: 28px; font-weight: 700; letter-spacing: 0.5px;
  }
  .news-list {
    position: absolute; left: 390px; top: 494px; width: 252px;
    color: var(--white); font-size: 15px; line-height: 1.25; text-align: justify;
  }
  .news-list li { margin-bottom: 2px; }

  .photo { position: absolute; }
  .photo--building {
    left: 372px; top: 630px; width: 278px; height: 82px;
    background: linear-gradient(180deg, #b9cfe0 0%, #cfd6d6 45%, #e8e0c8 70%, #a9a79c 100%);
  }
  .photo--doctor {
    left: 40px; top: 540px; width: 320px; height: 320px;
    background: linear-gradient(180deg, #dfe6ee 0%, #ffffff 40%, #b8cce6 75%, #2d3f74 100%);
  }

  .call { position: absolute; right: 40px; bottom: 46px; color: var(--white); text-align: right; }
  .call-label { font-size: 20px; font-weight: 700; }
  .call-number { font-size: 32px; font-weight: 700; margin-top: 2px; }
</style>
</head>
<body>
  <article class="flyer">
    <svg class="flyer-bands" width="660" height="860" viewBox="0 0 660 860" aria-hidden="true">
      <defs>
        <linearGradient id="blueGrad" x1="0" y1="0" x2="1" y2="1">
          <stop offset="0" stop-color="#2c55aa"/>
          <stop offset="1" stop-color="#1b2d86"/>
        </linearGradient>
      </defs>
      <path d="M0 0 H660 V135 L300 175 L0 205 Z" fill="url(#blueGrad)"/>
      <path d="M0 205 L300 175 L660 135 V147 L300 187 L0 217 Z" fill="var(--green)"/>
      <path d="M0 470 L660 385 V435 L0 520 Z" fill="url(#blueGrad)"/>
      <path d="M0 520 L660 435 V860 H0 Z" fill="var(--green)"/>
      <path d="M360 762 L660 730 V860 H360 Z" fill="url(#blueGrad)"/>
      <path d="M360 750 L660 718 V730 L360 762 Z" fill="#ffffff"/>
    </svg>

    <header>
      <div class="brand-mark" aria-hidden="true"></div>
      <div class="brand">
        <h1 class="brand-name">Meadowbrook Medical Center</h1>
        <p class="brand-contact">4410 Linden Ave. Maple Grove, CA, 90310 &nbsp; Fax (555) 014-2290</p>
      </div>
    </header>

    <section class="services">
      <h2 class="services-title">SERVICES</h2>
      <ul class="service-list service-list--right">
        <li>Pregnancy test</li>
        <li>Hiv / std test</li>
        <li>Mammograms</li>
        <li>Other services available</li>
      </ul>
      <ul class="service-list service-list--left">
        <li>Physical exam for immigration</li>
        <li>Blood pressure test</li>
        <li>Prenatal care evaluation to lose weight</li>
      </ul>
    </section>

    <section class="news">
      <h2 class="news-title">NEW FROM US !!</h2>
      <ul class="news-list">
        <li>Now accepting pi cases on lien!</li>
        <li>Same and next business day appointments available for initial visits, pre-operative clearances, and all other medical needs</li>
        <li>Expedited medical reports sent quickly to your office</li>
      </ul>
    </section>

    <div class="photo photo--building" role="img" aria-label="Photo of the clinic building exterior"></div>
    <div class="photo photo--doctor" role="img" aria-label="Portrait of the doctor in a white coat with a stethoscope"></div>

    <footer class="call">
      <p class="call-label">Call Us At :</p>
      <p class="call-number">(555) 014-2288</p>
    </footer>
  </article>
</body>
</html>
```